Harbor Crest Solutions Letterhead Design

The project name sums it up. Just need a professional letterhead design / template we can use in our marketing folders.

Here's the address / contact info for the letterhead: Harbor Crest Solutions 4817 Maple Ridge Dr Suite 150 Cedar Bay, Vermont 77419 555-508-7364 www.harborcrestsolutions.us support@harborcrestsolutions.us

```html
<!DOCTYPE html>
<html lang="en">
<head>
<meta charset="utf-8">
<title>Harbor Crest Solutions Letterhead</title>
<link href="https://fonts.googleapis.com/css2?family=Roboto:wght@400;700&display=swap" rel="stylesheet">
<style>
  :root {
    --backdrop: #d8cab0;
    --paper: #ffffff;
    --ink: #222222;
    --ink-soft: #444444;
    --brand-blue: #1655b3;
    --band-black: #111111;
    --signature-tone: #d9d9d9;
  }
  * { box-sizing: border-box; margin: 0; padding: 0; }
  html, body { width: 1200px; height: 898px; overflow: hidden; }
  body {
    background: var(--backdrop);
    font-family: "Roboto", Arial, sans-serif;
    color: var(--ink);
    display: flex; align-items: center; justify-content: center;
  }
  .letterhead {
    position: relative;
    width: 608px; height: 860px;
    background: var(--paper);
    box-shadow: 0 6px 24px rgba(0,0,0,.18);
    overflow: hidden;
  }
  .brand {
    position: absolute; left: 52px; top: 92px;
    display: flex; align-items: center; gap: 10px;
  }
  .brand-dot { width: 34px; height: 34px; border-radius: 50%; background: var(--brand-blue); }
  .brand-name { font-size: 22px; font-weight: 700; color: var(--band-black); }
  .contact {
    position: absolute; left: 376px; top: 28px;
    border-left: 1.5px solid var(--brand-blue);
    padding: 24px 0 4px 16px;
    font-size: 9.5px; line-height: 1.45; color: var(--ink);
    font-style: normal;
  }
  .contact-company { color: var(--brand-blue); font-weight: 700; }
  .contact-lines { margin-bottom: 8px; }
  .contact-item { display: flex; align-items: center; gap: 6px; }
  .contact-item svg { width: 10px; height: 10px; fill: var(--brand-blue); flex: none; }
  .letter {
    position: absolute; left: 80px; top: 272px; width: 450px;
    font-size: 10.5px; line-height: 1.42; color: var(--ink-soft);
  }
  .recipient { margin-bottom: 12px; }
  .recipient-name { font-weight: 700; color: var(--ink); }
  .letter p { margin-bottom: 14px; }
  .closing { margin-top: 20px; }
  .signature { margin-top: 14px; width: 140px; height: 34px; background: var(--signature-tone); border-radius: 4px; }
  .footer { position: absolute; left: 0; bottom: 0; width: 608px; height: 120px; }
  .footer-mark {
    position: absolute; left: 50%; bottom: 44px; transform: translateX(-50%);
    display: flex; align-items: center; gap: 6px;
    font-size: 11px; font-weight: 700; color: var(--band-black);
    background: var(--paper); padding: 4px 10px;
    white-space: nowrap;
  }
  .footer-mark .dot { width: 14px; height: 14px; border-radius: 50%; background: var(--brand-blue); }
</style>
</head>
<body>
  <main class="letterhead">
    <header>
      <div class="brand">
        <span class="brand-dot"></span>
        <span class="brand-name">Harbor Crest Solutions</span>
      </div>
      <address class="contact">
        <div class="contact-lines">
          <div class="contact-company">Harbor Crest Solutions</div>
          <div>4817 Maple Ridge Dr Suite 150</div>
          <div>Cedar Bay, Vermont 77419</div>
        </div>
        <div class="contact-item"><svg viewBox="0 0 10 10"><path d="M2 0h2l1 2.5-1.3 1a6 6 0 0 0 2.8 2.8l1-1.3L10 6v2c0 1-1 2-2 2A8 8 0 0 1 0 2c0-1 1-2 2-2z"/></svg>555-508-7364</div>
        <div class="contact-item"><svg viewBox="0 0 10 10"><path d="M0 2h10v6H0zM0.8 2.6 5 5.6l4.2-3v0.9L5 6.5 0.8 3.5z" fill-rule="evenodd"/></svg>support@harborcrestsolutions.us</div>
        <div class="contact-item"><svg viewBox="0 0 10 10"><circle cx="5" cy="5" r="4.4" fill="none" stroke="#1655b3" stroke-width="1"/><path d="M0.6 5h8.8M5 0.6v8.8" stroke="#1655b3" stroke-width=".8"/></svg>www.harborcrestsolutions.us</div>
      </address>
    </header>

    <section class="letter">
      <div class="recipient">
        <div class="recipient-name">Someone Some body</div>
        <div>1001 Long Street</div>
        <div>New York City, USA</div>
      </div>
      <p>Dear Someone Somebody,</p>
      <p>Lorem ipsum dolor sit amet, consectetur adipiscing elit. Nunc ac magna tellus, vitae hendrerit mauris. Donec consectetur rhoncus nunc, vitae imperdiet leo viverra ut. Pellentesque fermentum mi ac erat ultricies faucibus. Nam gravida nibh non lacus fermentum porta. Nulla non placerat turpis. Maecenas quis metus sem. Nullam nisi lacus, egestas sit amet porttitor nec, consectetur eget neque. Vivamus ultricies ultrices turpis, vel porttitor odio sagittis a. Pellentesque accumsan, lacus at suscipit rutrum, erat tortor imperdiet purus, semper congue augue turpis eget est. Curabitur blandit, orci ut accumsan fermentum, lorem metus auctor nisl, eget sodales elit libero id mi. Nullam sed lorem augue, ut tristique dui.</p>
      <p>Pellentesque vehicula pulvinar libero et ultricies. In hac habitasse platea dictumst. Phasellus eget quam lectus, pellentesque condimentum nulla. Morbi consequat euismod purus ut auctor. Cras convallis eleifend vehicula. Sed facilisis egestas accumsan. Duis in blandit velit. Curabitur diam eros, volutpat et iaculis ut, suscipit at est.</p>
      <p>Aenean id diam enim. Donec vitae arcu quam. Nunc mollis feugiat pretium. Praesent vel ligula felis. Ut sed velit nibh. Suspendisse faucibus convallis scelerisque. Sed sodales, nisi vitae placerat eleifend, lorem nulla iaculis leo, in lacinia metus sem quis purus. Ut non felis felis, pharetra fermentum purus. Suspendisse potenti. Nunc non faucibus ligula. Phasellus ipsum velit, laoreet ut scelerisque vel, commodo at felis. Donec malesuada malesuada aliquam. Aliquam justo elit, dapibus vitae hendrerit hendrerit, commodo sed ipsum. Donec ultricies mi non felis sollicitudin et elementum augue adipiscing. Integer quam purus, venenatis in ornare ac, sagittis quis purus.</p>
      <div class="closing">Youre Sincerely,</div>
      <div class="signature" role="img" aria-label="Handwritten signature"></div>
    </section>

    <footer class="footer">
      <svg width="608" height="120" viewBox="0 0 608 120">
        <polygon points="0,88 250,88 262,78 346,78 358,88 608,88 608,94 358,94 346,84 262,84 250,94 0,94" fill="#111111"/>
        <polygon points="0,100 250,100 262,90 346,90 358,100 608,100 608,120 0,120" fill="#1655b3"/>
      </svg>
      <div class="footer-mark"><span class="dot"></span>Harbor Crest Solutions</div>
    </footer>
  </main>
</body>
</html>
```